online jewellery store business card

all black business card, glossy, with gold writing, gold logo and name (provided). simple design.

Target Market(s)

This business card is to put with purchases, so it just needs the logo and name Solvane Jewellery which I have uploaded pictures for you to use. Then it needs the web address, markolo address, email address and then the like us on CH for 10% off. All words to be used have been provided. Thanks

Industry/Entity Type

Store

Contact Information for Business Card

www.solvanejewellery.com
stores.markolo.com.au/Solvane-Jewellery
info@solvanejewellery.com

Like us on chatterly for 10% off your next purchase!

Requirements
Must have
• black background
gold writing
glossy look
Should not have
• yellow writing

```html
<!DOCTYPE html>
<html lang="en">
<head>
<meta charset="utf-8">
<title>Solvane Jewellery — Business Card</title>
<link href="https://fonts.googleapis.com/css2?family=Josefin+Sans:wght@300;400&family=Arimo:wght@400&display=swap" rel="stylesheet">
<style>
  :root {
    --page: #e7e3dc;
    --card-black: #0b0b0b;
    --panel-black: #151515;
    --panel-deep: #050505;
    --gold: #c6a35a;
    --gold-light: #e2c47f;
    --gold-dark: #9c7a38;
    --gold-muted: #8d7645;
  }
  * { box-sizing: border-box; margin: 0; padding: 0; }
  html, body { width: 1200px; height: 900px; overflow: hidden; }
  body {
    background: var(--page);
    display: flex;
    align-items: center;
    justify-content: center;
    gap: 60px;
  }
  .card {
    position: relative;
    width: 540px;
    height: 309px;
    background: linear-gradient(150deg, #1a1a1a 0%, var(--card-black) 45%, #000 100%);
    border-radius: 3px;
    overflow: hidden;
    box-shadow: 0 10px 24px rgba(0,0,0,0.28);
  }
  .card::after {
    content: "";
    position: absolute;
    inset: 0;
    background: linear-gradient(125deg, rgba(255,255,255,0.08) 0%, rgba(255,255,255,0) 40%);
    pointer-events: none;
  }

  /* Front */
  .card-front {
    display: flex;
    flex-direction: column;
    align-items: center;
    justify-content: center;
    gap: 20px;
  }
  .brand-mark {
    width: 82px;
    height: 82px;
    border-radius: 50%;
    border: 2px solid var(--gold-muted);
  }
  .brand-name {
    font-family: "Josefin Sans", sans-serif;
    font-weight: 300;
    color: var(--gold-muted);
    text-transform: uppercase;
    text-align: center;
    letter-spacing: 0.32em;
    line-height: 1.15;
  }
  .card-front .brand-name { font-size: 34px; padding-left: 0.32em; }

  /* Back */
  .card-back { display: flex; }
  .gold-band {
    width: 62px;
    background: linear-gradient(90deg, var(--gold-dark), var(--gold-light) 50%, var(--gold));
  }
  .back-body {
    flex: 1;
    position: relative;
    padding: 22px 22px 18px 18px;
    display: flex;
    flex-direction: column;
  }
  .info-panel {
    flex: 1;
    display: flex;
    background: var(--panel-black);
    border-radius: 2px;
  }
  .identity {
    width: 190px;
    display: flex;
    flex-direction: column;
    align-items: center;
    justify-content: center;
    gap: 12px;
  }
  .identity .brand-mark { width: 46px; height: 46px; border-color: var(--gold); border-width: 1.5px; }
  .identity .brand-name { color: var(--gold); font-weight: 400; font-size: 16px; letter-spacing: 0.2em; padding-left: 0.2em; }
  .divider {
    width: 1px;
    margin: 30px 0;
    background: linear-gradient(180deg, transparent, var(--gold) 50%, transparent);
  }
  .contact-list {
    list-style: none;
    flex: 1;
    display: flex;
    flex-direction: column;
    justify-content: center;
    gap: 14px;
    padding: 0 14px 0 20px;
    font-family: "Arimo", sans-serif;
    font-size: 11.5px;
    color: var(--gold-light);
  }
  .offer-strip {
    margin-top: 12px;
    padding: 12px 14px;
    background: var(--panel-deep);
    font-family: "Arimo", sans-serif;
    font-size: 15px;
    color: var(--gold);
    text-align: center;
  }
</style>
</head>
<body>
  <section class="card card-front" aria-label="Card front">
    <div class="brand-mark" aria-hidden="true"></div>
    <h1 class="brand-name">Solvane<br>Jewellery</h1>
  </section>

  <section class="card card-back" aria-label="Card back">
    <div class="gold-band"></div>
    <div class="back-body">
      <div class="info-panel">
        <div class="identity">
          <div class="brand-mark" aria-hidden="true"></div>
          <h2 class="brand-name">Solvane<br>Jewellery</h2>
        </div>
        <div class="divider"></div>
        <ul class="contact-list">
          <li>stores.markolo.com.au/Solvane-Jewellery</li>
          <li>www.solvanejewellery.com</li>
          <li>info@solvanejewellery.com</li>
        </ul>
      </div>
      <p class="offer-strip">Like us on chatterly for 10% off your next purchase!</p>
    </div>
  </section>
</body>
</html>
```